Borrowdale Equity Business Card

Looking for a design for our business cards. Need to look corporate and outstanding. I have enclosed our logos for the company. Borrowdale equity is an investment firm for high level clients looking for advisory in their investments. White background or black is good. We will like to double sided options maybe at the back with just the logo of the firm.

Example of the info for the business card:

Marcus Heller
Managing Director

Panama Phone +507 391 4786
Switzerland Phone +41 43 917 2648
test@borrowdale-equity-example.com
www.borrowdale-equity-example.com

Industry/Entity Type

Investment

```html
<!DOCTYPE html>
<html lang="en">
<head>
<meta charset="utf-8">
<title>Borrowdale Equity Business Card</title>
<link rel="stylesheet" href="https://fonts.googleapis.com/css2?family=Open+Sans:wght@400;600&display=swap">
<style>
  :root {
    --stage: #ecebe8;
    --card-white: #ffffff;
    --card-black: #0e0f12;
    --card-black-soft: #1c1d22;
    --navy: #2c3d8c;
    --gold: #b38c3c;
    --ink: #1a1a1a;
    --title-ink: #333333;
  }
  * { box-sizing: border-box; margin: 0; padding: 0; }
  html, body {
    width: 1200px;
    height: 784px;
    overflow: hidden;
    background: var(--stage);
    font-family: "Open Sans", Arial, sans-serif;
  }
  .stage {
    position: relative;
    width: 1200px;
    height: 784px;
    display: flex;
    align-items: center;
    justify-content: center;
    gap: 28px;
  }
  .card {
    position: relative;
    width: 558px;
    height: 319px;
    overflow: hidden;
    box-shadow: 0 6px 18px rgba(0, 0, 0, 0.18);
  }

  /* Back side */
  .card-back {
    background: radial-gradient(ellipse at 45% 40%, var(--card-black-soft) 0%, var(--card-black) 70%);
    display: flex;
    align-items: center;
    justify-content: center;
  }

  /* Wordmark */
  .wordmark {
    display: flex;
    align-items: center;
    gap: 14px;
    color: var(--navy);
    font-weight: 600;
  }
  .wordmark-square {
    width: 30px;
    height: 30px;
    background: var(--navy);
  }
  .wordmark-name {
    font-size: 26px;
    letter-spacing: 0.06em;
    text-transform: uppercase;
    line-height: 1;
  }
  .card-back .wordmark-name { font-size: 28px; }

  /* Front side */
  .card-front { background: var(--card-white); }
  .card-front .wordmark {
    position: absolute;
    left: 56px;
    top: 52px;
  }
  .contact {
    position: absolute;
    left: 58px;
    top: 150px;
    color: var(--ink);
  }
  .contact-name {
    color: var(--navy);
    font-size: 19px;
    font-weight: 600;
    line-height: 1.1;
  }
  .contact-title {
    font-size: 11px;
    color: var(--title-ink);
    margin-top: 2px;
  }
  .contact-lines {
    list-style: none;
    margin-top: 14px;
    font-size: 13.5px;
    line-height: 1.3;
  }
  .footer-band {
    position: absolute;
    left: 0;
    right: 0;
    bottom: 0;
    height: 30px;
    background: var(--card-black);
    border-top: 3px solid var(--gold);
  }
</style>
</head>
<body>
  <main class="stage">
    <section class="card card-back" aria-label="Business card back">
      <div class="wordmark">
        <span class="wordmark-square"></span>
        <span class="wordmark-name">Borrowdale Equity</span>
      </div>
    </section>

    <section class="card card-front" aria-label="Business card front">
      <div class="wordmark">
        <span class="wordmark-square"></span>
        <span class="wordmark-name">Borrowdale Equity</span>
      </div>
      <div class="contact">
        <p class="contact-name">Marcus Heller</p>
        <p class="contact-title">Managing Director</p>
        <ul class="contact-lines">
          <li>Panama Phone +507 391 4786</li>
          <li>Switzerland Phone +41 43 917 2648</li>
          <li>test@borrowdale-equity-example.com</li>
          <li>www.borrowdale-equity-example.com</li>
        </ul>
      </div>
      <div class="footer-band"></div>
    </section>
  </main>
</body>
</html>
```